Design a large parking banner – mandatory ticket validation in the shop

Banner Size:
548 cm (width) x 154 cm (height)
Note: The banner will be placed in a metal frame at our parking lot entrance, fully visible to every incoming truck driver. The message must be easy to read from a distance.
Goal of the Banner:
To inform all truck drivers that they must validate their entry ticket inside the shop, even if they are parking for a short time.
The message must be displayed in multiple languages for international drivers.
Mandatory Content:
Main message – in multiple languages (clearly separated or stacked):
Dutch (NL): Vergeet je ticket niet te valideren in de shop – verplicht, ook bij kort parkeren!
French (FR): N'oubliez pas de valider votre ticket à la boutique – obligatoire, même pour un court arrêt !
English (EN): Don't forget to validate your entry ticket in the shop – mandatory, even for short stops!
German (DE): Vergessen Sie nicht, Ihr Einfahrticket im Shop zu entwerten – Pflicht, auch bei kurzem Parken!
Polish (PL): Nie zapomnij zatwierdzić biletu w sklepie – obowiązkowe, nawet przy krótkim postoju!
Romanian (RO): Nu uitați să validați biletul în magazin – obligatoriu, chiar și pentru opriri scurte!
You can include more languages if space allows, but these are essential.
Opening Hours Block (in one section below):
Shop Opening Hours
Mon – Fri: 05:30 – 22:00
Sat & Sun: 08:00 – 22:00
Style & Branding:
The design must match the visual identity of Haulpoint 41Ter
Please refer to the attached photos of existing parking signage for guidance on colors, typography, and layout style
Our logo (attached) must be clearly visible and professionally integrated
Feel free to use icons or pictograms to visually support the message (e.g., ticket, truck, arrow)
Readability is key – large, bold text and high contrast colors that are visible from a distance
Target Audience:
International truck drivers – people who need fast, clear communication. Not everyone speaks the local language, so visual clarity and multilingual messaging are critical.
File Requirements:
Print-ready file (PDF or EPS) – 300 dpi at 1:10 scale
Include 5 cm bleed on all sides
Provide open source files if possible (AI or PSD)

```html
<!DOCTYPE html>
<html lang="en">
<head>
<meta charset="utf-8">
<title>Haulpoint 41Ter – Ticket Validation Banner</title>
<link href="https://fonts.googleapis.com/css2?family=Poppins:wght@500;600;700;800&display=swap" rel="stylesheet">
<style>
  :root {
    --stage: #a6a6a6;
    --navy: #363962;
    --blue: #2f80c3;
    --red: #f20000;
    --label-red: #e3101a;
    --white: #ffffff;
  }
  * { box-sizing: border-box; margin: 0; padding: 0; }
  html, body {
    width: 1200px; height: 536px; overflow: hidden;
    background: var(--stage);
    font-family: "Poppins", sans-serif;
  }
  .banner {
    position: absolute; left: 0; top: 55px;
    width: 1200px; height: 425px;
    background: var(--navy);
    color: var(--white);
  }
  .brand {
    position: absolute; left: 84px; top: 80px; width: 380px;
    display: flex; align-items: center; gap: 14px;
  }
  .brand-mark {
    width: 34px; height: 34px; background: var(--blue); flex: none;
  }
  .brand-name {
    font-weight: 800; font-size: 50px; line-height: 1.05;
    color: var(--white); letter-spacing: -1px;
  }
  .parking-label {
    position: absolute; left: 37px; top: 265px;
    display: flex; align-items: center; gap: 17px;
  }
  .parking-label svg { width: 29px; height: 55px; }
  .parking-label span { font-weight: 600; font-size: 30px; letter-spacing: -0.5px; line-height: 1; }
  .down-arrow { position: absolute; left: 95px; top: 349px; width: 55px; height: 39px; }
  .ticket-label {
    position: absolute; left: 204px; top: 314px;
    font-weight: 600; font-size: 43px; letter-spacing: -1px; line-height: 1;
    white-space: nowrap;
  }
  .ticket-icon { position: absolute; left: 395px; top: 271px; width: 106px; height: 112px; }
  .messages {
    position: absolute; left: 531px; top: 27px; width: 650px;
    list-style: none;
  }
  .messages li {
    height: 34.4px; font-size: 12.4px; font-weight: 600;
    letter-spacing: -0.35px; white-space: nowrap;
  }
  .messages .lang { color: var(--label-red); }
  .hours-title, .style-note {
    position: absolute; left: 540px; width: 631px;
    background: var(--blue); text-align: center;
    font-weight: 600; font-size: 27px; letter-spacing: -0.5px;
  }
  .hours-title { top: 250px; height: 47px; line-height: 47px; }
  .style-note { top: 358px; height: 47px; line-height: 47px; }
  .hours-row {
    position: absolute; left: 540px; top: 302px; width: 631px; height: 44px;
    display: flex; gap: 2px;
  }
  .hours-slot {
    flex: 1; background: var(--red); text-align: center;
    font-weight: 600; font-size: 26px; line-height: 44px; letter-spacing: -0.5px;
    white-space: nowrap;
  }
</style>
</head>
<body>
<main class="banner">
  <div class="brand">
    <div class="brand-mark"></div>
    <div class="brand-name">Haulpoint<br>41Ter</div>
  </div>

  <div class="parking-label">
    <svg viewBox="0 0 29 55" aria-hidden="true">
      <rect width="29" height="55" rx="4" fill="var(--blue)"/>
      <text x="14.5" y="38" text-anchor="middle" font-family="Poppins, sans-serif" font-weight="800" font-size="26" fill="#fff">P</text>
    </svg>
    <span>TRUCKS</span>
  </div>
  <svg class="down-arrow" viewBox="0 0 56 40" aria-hidden="true">
    <polygon points="0,4 8,0 28,20 48,0 56,4 28,40" fill="var(--white)"/>
  </svg>

  <div class="ticket-label">+ TICKET</div>
  <svg class="ticket-icon" viewBox="0 0 106 113" aria-hidden="true">
    <polygon points="20,30 82,0 90,22 40,46" fill="var(--white)"/>
    <path d="M0,48 H106 V70 A10,10 0 0 0 106,90 V113 H0 V90 A10,10 0 0 0 0,70 Z" fill="var(--white)"/>
    <rect x="18" y="62" width="44" height="34" fill="var(--navy)"/>
    <rect x="25" y="69" width="30" height="6" fill="var(--white)"/>
    <rect x="25" y="82" width="30" height="8" fill="var(--white)"/>
    <rect x="72" y="58" width="4" height="44" fill="var(--navy)"/>
  </svg>

  <ul class="messages">
    <li><span class="lang">Dutch (NL):</span> Vergeet je ticket niet te valideren in de shop – verplicht, ook bij kort parkeren!</li>
    <li><span class="lang">French (FR):</span> N'oubliez pas de valider votre ticket à la boutique – obligatoire, même pour un court arrêt !</li>
    <li><span class="lang">English (EN):</span> Don't forget to validate your entry ticket in the shop – mandatory, even for short stops!</li>
    <li><span class="lang">German (DE):</span> Vergessen Sie nicht, Ihr Einfahrticket im Shop zu entwerten – Pflicht, auch bei kurzem Parken!</li>
    <li><span class="lang">Polish (PL):</span> Nie zapomnij zatwierdzić biletu w sklepie – obowiązkowe, nawet przy krótkim postoju!</li>
    <li><span class="lang">Romanian (RO):</span> Nu uitați să validați biletul în magazin – obligatoriu, chiar și pentru opriri scurte!</li>
  </ul>

  <div class="hours-title">Shop Opening Hours</div>
  <div class="hours-row">
    <div class="hours-slot">Mon – Fri: 05:30 – 22:00</div>
    <div class="hours-slot">Sat &amp; Sun: 08:00 – 22:00</div>
  </div>
  <div class="style-note">Style &amp; Branding:</div>
</main>
</body>
</html>
```